Reed & Vale NC grand opening (for BILLBOARD)

Advertising the grand opening of our cannabis/hemp shop in NC. We will sell all things hemp (flower, cartridges, disposables, edibles, creams, lotions, pet products etc...)

Requirements
Must have
• include, open starting Aug 1, but grand opening Aug 15th.
Nice to have
• Difference slogan ideas "Save some cash, buy our grass" "Find your perfect high at Reed & Vale cannabis store" "Experience Nature's Gift: Reed & Vale Cannabis Store"

```html
<!DOCTYPE html>
<html lang="en">
<head>
<meta charset="utf-8">
<title>Reed &amp; Vale Billboard</title>
<link href="https://fonts.googleapis.com/css2?family=Poppins:wght@400;600&display=swap" rel="stylesheet">
<style>
  :root {
    --page: #ffffff;
    --leaf-green: #7dc142;
    --foliage-dark: #1f8a3a;
    --foliage-light: #4fb548;
    --navy: #1b1a3d;
    --white: #ffffff;
  }
  html, body {
    margin: 0;
    padding: 0;
    width: 1200px;
    height: 1200px;
    overflow: hidden;
    background: var(--page);
  }
  .canvas {
    position: relative;
    width: 1200px;
    height: 1200px;
    background: var(--page);
  }
  .billboard {
    position: absolute;
    left: 77px;
    top: 446px;
    width: 1046px;
    height: 307px;
    background: var(--leaf-green);
    overflow: hidden;
    font-family: "Poppins", sans-serif;
  }
  .foliage {
    position: absolute;
    top: 0;
    height: 100%;
  }
  .foliage--left {
    left: 0;
    width: 180px;
    background: linear-gradient(90deg, var(--foliage-dark) 0%, var(--foliage-light) 60%, rgba(125,193,66,0) 100%);
  }
  .foliage--right {
    right: 0;
    width: 265px;
    background: linear-gradient(270deg, var(--foliage-dark) 0%, var(--foliage-light) 60%, rgba(125,193,66,0) 100%);
  }
  .headline {
    position: absolute;
    left: 187px;
    top: 45px;
    margin: 0;
    font-size: 51px;
    line-height: 52px;
    font-weight: 600;
    letter-spacing: 0;
    text-transform: uppercase;
    color: var(--white);
    white-space: nowrap;
  }
  .headline .accent { color: var(--navy); }
  .brand-card {
    position: absolute;
    left: 647px;
    top: 0;
    width: 244px;
    height: 130px;
    background: var(--white);
    border-radius: 0 0 10px 10px;
    box-shadow: 0 3px 8px rgba(0,0,0,0.18);
    display: flex;
    align-items: center;
    justify-content: center;
  }
  .brand-name {
    font-size: 34px;
    font-weight: 600;
    color: var(--navy);
    letter-spacing: -0.5px;
  }
  .opening-dates {
    position: absolute;
    left: 647px;
    top: 146px;
    margin: 0;
    font-size: 18px;
    line-height: 34px;
    font-weight: 600;
    color: var(--navy);
    white-space: nowrap;
  }
  .location-band {
    position: absolute;
    left: 647px;
    right: 0;
    top: 198px;
    height: 58px;
    background: var(--navy);
    display: flex;
    align-items: center;
    padding-left: 22px;
    gap: 8px;
    color: var(--leaf-green);
    font-size: 19px;
    font-weight: 400;
  }
  .location-band svg { width: 16px; height: 22px; }
</style>
</head>
<body>
<div class="canvas">
  <section class="billboard">
    <div class="foliage foliage--left" role="img" aria-label="Photo of green cannabis leaves"></div>
    <div class="foliage foliage--right" role="img" aria-label="Photo of green cannabis plants"></div>

    <h1 class="headline">
      Find your<br>
      <span class="accent">Perfect high</span><br>
      At <span class="accent">Reed &amp; Vale</span><br>
      Cannabis store
    </h1>

    <div class="brand-card">
      <span class="brand-name">Reed &amp; Vale</span>
    </div>

    <p class="opening-dates">Open Aug 1 &middot; Grand Opening Aug 15</p>

    <div class="location-band">
      <svg viewBox="0 0 16 22" aria-hidden="true">
        <path d="M8 0C3.6 0 0 3.5 0 7.9 0 13.6 8 22 8 22s8-8.4 8-14.1C16 3.5 12.4 0 8 0zm0 11a3.2 3.2 0 1 1 0-6.4A3.2 3.2 0 0 1 8 11z" fill="currentColor"/>
      </svg>
      <span class="location-text">Exit 4B Maple Ridge Rd</span>
    </div>
  </section>
</div>
</body>
</html>
```